Torven Medical needs bold attention catching website for healthcare professionals(target)

I need a hero page as well as a products and about page for a website of mine. I specialize in orthopedic instruments . Specifically bone drills and saws. This whole company was founded to bring superb quality highly discounted medical instruments. Specifically bone drills, bone saws, k-wires and pins. Two main points should be cost savings and superior quality.

Target Market(s)

healthcare professionals Surgeons and hospital material managers

Number of Pages Required

3 page

Font styles to use
Serif

Colors

Designer to choose colors to be used in the design.

Requirements
Must have
• colors should match logo design

```html
<!DOCTYPE html>
<html lang="en">
<head>
<meta charset="utf-8">
<title>Torven Medical</title>
<link href="https://fonts.googleapis.com/css2?family=Oxygen:wght@400;700&family=Lato:wght@400;700&display=swap" rel="stylesheet">
<style>
:root{
  --orange:#f7820f;
  --orange-dark:#e96f00;
  --ink:#333333;
  --text:#555555;
  --muted:#9a9a9a;
  --panel:#f8f8f8;
  --line:#d8d8d8;
  --footer:#0b0b0b;
  --footer-bar:#1d1d1d;
  --white:#ffffff;
}
*{box-sizing:border-box;margin:0;padding:0}
html,body{width:1200px;height:3636px;overflow:hidden;background:var(--white)}
body{position:relative;font-family:'Lato',sans-serif;color:var(--text)}
.abs{position:absolute}
.heading{font-family:'Oxygen',sans-serif;color:var(--ink);font-weight:400}
.btn{position:absolute;display:flex;align-items:center;justify-content:center;background:var(--orange);color:var(--white);font-family:'Oxygen',sans-serif;font-weight:700;font-size:14px;border-radius:22px}
.copy{font-size:11px;line-height:21px;color:var(--text)}

/* header */
.site-header{left:0;top:0;width:1200px;height:97px;background:var(--white)}
.site-header .rule{position:absolute;left:0;top:92px;width:1200px;height:4px;background:var(--orange)}
.brand{position:absolute;display:flex;align-items:center;gap:8px;font-family:'Oxygen',sans-serif;font-size:21px;color:var(--ink);letter-spacing:.5px}
.brand .dot{width:12px;height:12px;border-radius:50%;background:var(--orange)}
.nav{position:absolute;top:45px;display:flex;font-family:'Oxygen',sans-serif;font-size:13px;color:var(--orange)}
.nav span{position:absolute;white-space:nowrap}

/* hero */
.hero{left:0;top:97px;width:1200px;height:503px;background:linear-gradient(100deg,#2c3e4c 0%,#3e4a52 30%,#1f3140 55%,#2d4456 80%,#22384a 100%)}
.hero-title{left:0;width:1200px;top:288px;text-align:center;font-family:'Oxygen',sans-serif;font-weight:700;font-size:64px;color:var(--white)}
.hero-sub{left:0;width:1200px;top:370px;text-align:center;font-family:'Oxygen',sans-serif;font-size:23px;color:var(--orange)}

/* about */
.about-photo{left:95px;top:676px;width:366px;height:387px;background:linear-gradient(135deg,#eef1f4,#d9dee4 60%,#c9cfd6)}
.about-edge{left:461px;top:676px;width:4px;height:387px;background:var(--orange)}

/* specialisation rings */
.ring{position:absolute;width:100px;height:100px}
.ring span{position:absolute;inset:0;display:flex;align-items:center;justify-content:center;font-family:'Oxygen',sans-serif;font-size:33px;color:var(--ink)}

/* products */
.products{left:0;top:1487px;width:1200px;height:428px;background:linear-gradient(180deg,#9aa6ae 0%,#b9c0c3 40%,#8b9ca6 75%,#5d7787 100%)}
.product-card{position:absolute;top:1607px;width:240px;height:243px;border:1px solid rgba(255,255,255,.55)}
.product-card .shot{height:187px}
.product-card .label{height:56px;display:flex;align-items:center;justify-content:center;color:var(--orange);font-family:'Oxygen',sans-serif;font-size:17px}

/* blog */
.blog-card{position:absolute;top:2124px;width:323px;height:419px;background:var(--panel)}
.blog-card .thumb{position:absolute;left:56px;top:34px;width:210px;height:210px;border-radius:50%;border:5px solid var(--white);box-shadow:0 0 8px rgba(0,0,0,.08)}
.blog-card .date{position:absolute;left:46px;top:278px;font-family:'Oxygen',sans-serif;font-size:17px;color:var(--ink)}
.blog-card .title{position:absolute;left:182px;top:276px;font-family:'Oxygen',sans-serif;font-size:18px;color:var(--orange)}
.blog-card .excerpt{position:absolute;left:18px;top:320px;width:287px;text-align:center;font-size:11px;line-height:18px}

/* contact */
.contact-panel{left:325px;top:2620px;width:774px;height:557px;background:var(--panel);box-shadow:0 2px 14px rgba(0,0,0,.12)}
.contact-card{left:161px;top:2681px;width:312px;height:435px;background:linear-gradient(160deg,#3d5866,#4a5b5e 55%,#3a4f5c)}
.contact-card .row{position:absolute;left:58px;display:flex;gap:12px;color:var(--white);font-size:11px;line-height:18px}
.field{position:absolute;left:540px;width:472px;background:var(--white);border:1px solid var(--line);border-radius:4px;font-size:11px;color:#b5b5b5;padding:12px 20px}

/* footer */
.site-footer{left:0;top:3243px;width:1200px;height:373px;background:var(--footer)}
.footer-bar{left:0;top:3616px;width:1200px;height:20px;background:var(--footer-bar);color:var(--white);font-size:10px;text-align:center;line-height:20px}
.foot-head{position:absolute;font-family:'Oxygen',sans-serif;font-size:17px;color:var(--white)}
.foot-text{position:absolute;color:#dddddd;font-size:10.5px;line-height:18px}
.foot-link{position:absolute;left:456px;color:var(--white);font-size:11px;display:flex;align-items:center;gap:10px}
.news-thumb{position:absolute;left:609px;width:54px;height:48px;background:linear-gradient(135deg,#c9d6e2,#8ea6bb)}
.foot-field{position:absolute;left:885px;width:221px;border:1px solid #8a8a8a;color:#bbbbbb;font-size:8.5px;padding:6px 10px}
.social{position:absolute;top:3521px;width:28px;height:28px;border-radius:50%;background:var(--white)}
</style>
</head>
<body>

<header class="abs site-header">
  <div class="brand" style="left:95px;top:33px"><span class="dot"></span>Torven Medical</div>
  <svg class="abs" style="left:240px;top:0" width="70" height="96"><line x1="68" y1="0" x2="6" y2="94" stroke="var(--orange)" stroke-width="1.5"/></svg>
  <nav class="nav">
    <span style="left:557px">Home</span>
    <span style="left:650px">About us</span>
    <span style="left:759px">Products</span>
    <span style="left:868px">Blog</span>
    <span style="left:952px">Gallery</span>
    <span style="left:1052px">Contacts</span>
  </nav>
  <div class="rule"></div>
</header>

<section class="abs hero" role="img" aria-label="Surgical team operating in a hospital theatre"></section>
<h1 class="abs hero-title">Hospitals Are Increasingly</h1>
<p class="abs hero-sub">seeking ways to cut cost while continuing to deliver high quality medical care</p>
<a class="btn" style="left:531px;top:427px;width:138px;height:42px">Read More</a>

<!-- about -->
<div class="abs about-photo" role="img" aria-label="Two doctors reviewing an x-ray in a clinic"></div>
<div class="abs about-edge"></div>
<h2 class="abs heading" style="left:565px;top:697px;font-size:40px">About Us</h2>
<p class="abs copy" style="left:565px;top:758px;width:530px">Lorem ipsum dolor sit amet, consectetur adipiscing elit. Donec felis magna, maximus vitae auctor eget, bibendum id ligula. Orci varius natoque penatibus et magnis dis parturient montes, nascetur ridiculus mus. Curabitur consequat neque est, et semper purus tincidunt ac. Quisque est sapien, lacinia et pulvinar id, vehicula mattis mi. Nullam pulvinar, est eu dignissim rhoncus, tellus magna tempus lorem, quis aliquet metus orci nec arcu. Cras sed nisl vel massa convallis tincidunt quis id enim. Nullam non consequat nunc, id euismod mi. Duis pharetra nisl vitae lacus rhoncus malesuada. Praesent finibus rhoncus consequat.</p>
<p class="abs copy" style="left:565px;top:905px;width:530px">Vestibulum id erat id felis imperdiet placerat. Proin ultricies turpis a consequat luctus. Mauris ut erat eget felis ultrices facilisis eu sit amet mi. In at lorem cursus, eleifend sem a, imperdiet nisi. In a dui nisl. In gravida mauris et molestie vehicula. Integer dui nisi,</p>
<a class="btn" style="left:570px;top:992px;width:138px;height:44px">Read More</a>

<h2 class="abs heading" style="left:93px;top:1132px;font-size:42px;line-height:45px;font-weight:700">Why Doctor Choose<br>our Product</h2>
<p class="abs copy" style="left:95px;top:1245px;width:560px;font-size:10.5px;line-height:18px">Nunc non urna nec purus imperdiet egestas ac quis arcu. Aenean dui ante, semper nec tempor consequat, placerat vel diam. Morbi consequat aliquam gravida. Donec vitae accumsan ante. Aliquam eu eros et ligula bibendum suscipit. Integer tincidunt finibus erat non lacinia. Nulla vulputate bibendum lacinia. Donec ullamcorper convallis imperdiet. Sed nec condimentum ante.</p>
<a class="btn" style="left:95px;top:1362px;width:138px;height:46px">Read More</a>

<h3 class="abs heading" style="left:705px;top:1153px;font-size:26px">Our specialisations</h3>
<div class="ring" style="left:708px;top:1228px">
  <svg width="100" height="100"><circle cx="50" cy="50" r="48" fill="none" stroke="#eeeeee" stroke-width="3"/><path d="M50 2 A48 48 0 1 1 35 4.4" fill="none" stroke="var(--orange)" stroke-width="3"/></svg>
  <span>5%</span>
</div>
<div class="ring" style="left:847px;top:1228px">
  <svg width="100" height="100"><circle cx="50" cy="50" r="48" fill="none" stroke="#eeeeee" stroke-width="3"/><path d="M50 2 A48 48 0 1 1 22 11" fill="none" stroke="var(--orange)" stroke-width="3"/></svg>
  <span>10%</span>
</div>

<!-- products -->
<section class="abs products" role="img" aria-label="Blurred hospital corridor background"></section>
<h2 class="abs heading" style="left:0;width:1200px;top:1527px;text-align:center;font-size:40px;color:var(--white)">Product</h2>
<div class="product-card" style="left:95px"><div class="shot" role="img" aria-label="Bone drill in use" style="background:linear-gradient(135deg,#2f5773,#466b80 60%,#29475a)"></div><div class="label">Bone drills</div></div>
<div class="product-card" style="left:352px"><div class="shot" role="img" aria-label="Gloved hand holding k-wires" style="background:linear-gradient(135deg,#5d5650,#b4aca4 55%,#e8e6e4)"></div><div class="label">k-wires</div></div>
<div class="product-card" style="left:609px"><div class="shot" role="img" aria-label="Surgeons using a bone saw" style="background:linear-gradient(135deg,#3d7b8a,#7aa7ae 50%,#c9b7a4)"></div><div class="label">bone saws</div></div>
<div class="product-card" style="left:866px"><div class="shot" role="img" aria-label="Surgical pins on a light background" style="background:linear-gradient(135deg,#f2f2f2,#dfe3e6 50%,#f3c78f)"></div><div class="label">Pin</div></div>

<!-- blog -->
<h2 class="abs heading" style="left:0;width:1200px;top:1982px;text-align:center;font-size:42px">Blog</h2>
<p class="abs copy" style="left:200px;width:800px;top:2048px;text-align:center;line-height:18px">Lorem ipsum dolor sit amet, consectetur adipiscing elit. Donec felis magna, maximus vitae auctor eget,bibendum id ligula. Orci varius natoque penatibus et magnis dis parturient montes, nascetur ridiculus mus. Curabitur consequat neque est, et semper purus tincidunt ac</p>

<article class="blog-card" style="left:93px">
  <div class="thumb" role="img" aria-label="Tray of surgical instruments" style="background:linear-gradient(135deg,#3f6b8c,#9aa8b2 55%,#d4d8dc)"></div>
  <span class="date">01.09.19</span><span class="title">Lorem ipsum</span>
  <p class="excerpt">Lorem ipsum dolor sit amet, consectetur adipiscing elit. Donec felis magna, maximus vitae auctor eget, bibendum id ligula. Orci varius natoque penatibus et magnis dis parturient montes</p>
</article>
<article class="blog-card" style="left:438px">
  <div class="thumb" role="img" aria-label="Laparoscopic instruments close up" style="background:linear-gradient(135deg,#9fd1ea,#5fa5cc 55%,#e7c2b1)"></div>
  <span class="date">01.09.19</span><span class="title">Lorem ipsum</span>
  <p class="excerpt">Lorem ipsum dolor sit amet, consectetur adipiscing elit. Donec felis magna, maximus vitae auctor eget, bibendum id ligula. Orci varius natoque penatibus et magnis dis parturient montes</p>
</article>
<article class="blog-card" style="left:785px">
  <div class="thumb" role="img" aria-label="Assorted surgical clamps and scissors" style="background:linear-gradient(135deg,#6d93b6,#b8cbd9 55%,#3c5a7a)"></div>
  <span class="date">01.09.19</span><span class="title">Lorem ipsum</span>
  <p class="excerpt">Lorem ipsum dolor sit amet, consectetur adipiscing elit. Donec felis magna, maximus vitae auctor eget, bibendum id ligula. Orci varius natoque penatibus et magnis dis parturient montes</p>
</article>

<!-- contact -->
<section class="abs contact-panel"></section>
<div class="abs contact-card" role="img" aria-label="World map background">
  <h3 class="abs heading" style="left:58px;top:98px;font-size:30px;color:var(--white)">Contact US</h3>
  <div class="row" style="top:168px">
    <svg width="12" height="18" viewBox="0 0 12 18"><path d="M6 0a6 6 0 0 0-6 6c0 4.5 6 12 6 12s6-7.5 6-12a6 6 0 0 0-6-6zm0 8.5A2.5 2.5 0 1 1 6 3.5a2.5 2.5 0 0 1 0 5z" fill="#fff"/></svg>
    <span>418 Larkspur Ridge Rd, Ashford,<br>AZ, 85110</span>
  </div>
  <div class="row" style="top:238px">
    <svg width="18" height="13" viewBox="0 0 18 13"><rect x=".7" y=".7" width="16.6" height="11.6" fill="none" stroke="#fff" stroke-width="1.3"/><path d="M1 1l8 6 8-6" fill="none" stroke="#fff" stroke-width="1.3"/></svg>
    <span>info@torvenmedical.com</span>
  </div>
  <div class="row" style="top:303px">
    <svg width="18" height="18" viewBox="0 0 18 18"><path d="M4 1l3 4-2 2c1 2 3 4 5 5l2-2 4 3-2 3C8 16 2 10 1 4z" fill="none" stroke="#fff" stroke-width="1.4"/></svg>
    <span>555-014-2290</span>
  </div>
</div>
<h2 class="abs heading" style="left:536px;top:2664px;font-size:40px">Get&nbsp; Touch</h2>
<div class="field" style="top:2728px;height:40px">Name</div>
<div class="field" style="top:2779px;height:40px">Email</div>
<div class="field" style="top:2830px;height:40px">Phone</div>
<div class="field" style="top:2890px;height:172px">Message</div>
<a class="btn" style="left:877px;top:3077px;width:138px;height:46px;font-size:18px">Submit</a>

<!-- footer -->
<footer class="abs site-footer">
  <div class="brand" style="left:95px;top:90px;color:var(--white)"><span class="dot"></span>Torven Medical</div>
  <p class="foot-text" style="left:95px;top:156px;width:300px">Lorem ipsum dolor sit amet, consectetur adipiscing elit. Donec felis magna, maximus vitae auctor eget, bibendum id ligula. Orci varius natoque penatibus et magnis dis parturient montes, nascetur ridiculus mus. Curabitur consequat neque est,</p>

  <span class="foot-head" style="left:456px;top:64px">Sitemap</span>
  <span class="foot-link" style="top:122px">›&nbsp;Home</span>
  <span class="foot-link" style="top:145px">›&nbsp;About us</span>
  <span class="foot-link" style="top:168px">›&nbsp;Products</span>
  <span class="foot-link" style="top:191px">›&nbsp;Blog</span>
  <span class="foot-link" style="top:214px">›&nbsp;Gallery</span>
  <span class="foot-link" style="top:237px">›&nbsp;Contacts</span>

  <span class="foot-head" style="left:605px;top:64px">Newsletter</span>
  <div class="news-thumb" style="top:157px" role="img" aria-label="Doctors in a meeting"></div>
  <p class="foot-text" style="left:677px;top:157px;width:150px;color:#fff">Lorem ipsum dolor sit amet, consectetur adipiscing elit. Donec felis magna,</p>
  <div class="news-thumb" style="top:215px" role="img" aria-label="Doctor writing notes"></div>
  <p class="foot-text" style="left:677px;top:215px;width:150px;color:#fff">Lorem ipsum dolor sit amet, consectetur adipiscing elit. Donec felis magna,</p>
  <div class="news-thumb" style="top:275px" role="img" aria-label="Doctor consulting a patient"></div>
  <p class="foot-text" style="left:677px;top:275px;width:150px;color:#fff">Lorem ipsum dolor sit amet, consectetur adipiscing elit. Donec felis magna,</p>

  <span class="foot-head" style="left:883px;top:64px">Contact Us</span>
  <div class="foot-field" style="top:127px;height:25px">Enter Your Name</div>
  <div class="foot-field" style="top:159px;height:25px">Enter Your Email</div>
  <div class="foot-field" style="top:191px;height:25px">Enter Your Phone</div>
  <div class="foot-field" style="top:223px;height:52px">Massege</div>
  <a class="btn" style="left:993px;top:294px;width:113px;height:35px;font-size:17px">Submit</a>
</footer>
<span class="social" style="left:96px"></span>
<span class="social" style="left:134px"></span>
<span class="social" style="left:172px"></span>
<div class="abs footer-bar">©2019 Torven Medical ,All rights reserved</div>

</body>
</html>
```